Premium Wraparound Label Design for 6 oz Mellow Spread Jar – Lanakila Sweet Kitchen

Design a continuous wraparound label for an 6 oz circular glass jar that integrates the Lanakila Sweet Kitchen logo (featuring the pink and brown leaf motif) and the Mellow Spread nutrition label into one cohesive, premium presentation. The design should feel authentically Hawaiian, classic, and handcrafted—reflecting the brand’s legacy of island-inspired desserts.
Label Specifications
Container: 8 oz round glass jar
Label Type: Full wraparound (one continuous label)
Approximate Label Size: 2.5 inches tall × 8.5 inches wide
Finish: Matte or satin with optional gold foil highlights
Print: CMYK-ready artwork with bleed and safe zones clearly marked
Design Elements to Integrate
1. Front Panel (Main Display Area):
Prominently feature the Lanakila Sweet Kitchen logo centered and scaled proportionally.
Display the product name “Mellow Spread” in elegant, legible typography that complements the logo.
Add the following text beneath or near the product name:
“Made in Hawai‘i”
“Net Wt. 8 oz (227g)”
“Keep Refrigerated” (in smaller but clear type).
Background tones should complement the logo—cream, soft tan, or pastel pink for warmth and harmony.
The front should communicate island sophistication—premium yet inviting.
2. Side Panel (Transition Area):
Create a smooth visual transition around the jar using a subtle, continuous background pattern such as tropical leaves, ocean wave textures, or gold accent lines.
Include the brand story text:
“Lanakila Sweet Kitchen brings authentic island flavors to every table. Our signature Mellow Spread blends tropical fruit and fresh cream for a taste of pure aloha.”
3. Back Panel (Informational Area):
Integrate the Mellow Spread nutrition facts panel and ingredients list (from the attached file).
Ensure layout is FDA-compliant, legible, and well-balanced.
Beneath the ingredients, include:
“Manufactured by Lanakila Sweet Kitchen, Hawai‘i.”
“Keep Refrigerated.”
Leave space for:
A QR code linking to the brand website and social media.
A barcode area, placed neatly near the bottom or corner.
Aesthetic Direction
Style: Premium, classic, and island-inspired
Color Palette: Cream base with warm browns, muted pinks, and gold accents
Typography:
Serif or script for product name and logo (for a classic, handcrafted look)
Clean sans-serif for informational text
Mood: Heritage meets handcrafted luxury — nostalgic yet refined
Finish Options:
Matte for artisanal authenticity
Satin or metallic foil for a modern, premium touch
Deliverables
Designers should submit:
3 design variations (e.g., classic heritage, minimalist modern, and premium tropical).
Editable source files (AI, PSD, or layered PDF) with bleed and safe zones clearly marked.
Mockups on an 8 oz round glass jar for visual presentation.

Target Market(s)

Craft fair consumers / tourist in hawaii

Industry/Entity Type

food and Bev

Logo Text

see description

Font styles to use
Serif
Sans Serif
Script

Requirements
Must have
• see description
Nice to have
• see description
Should not have
• see description

```html
<!DOCTYPE html>
<html lang="en">
<head>
<meta charset="utf-8">
<title>Lanakila Sweet Kitchen – Mellow Spread Wraparound Label</title>
<link href="https://fonts.googleapis.com/css2?family=Roboto+Condensed:wght@300;400&family=Arimo:wght@400;700&display=swap" rel="stylesheet">
<style>
  :root{
    --backdrop-light:#ececec;
    --backdrop-dark:#d0d0d0;
    --cream:#e6dbcf;
    --brown:#512e11;
    --brown-text:#4a2a10;
    --pink:#d08a85;
    --cream-ink:#efe4d6;
    --gold-dark:#b8860b;
    --gold-light:#f7e08a;
    --ink:#231815;
  }
  *{margin:0;padding:0;box-sizing:border-box}
  html,body{width:1200px;height:1200px;overflow:hidden}
  body{position:relative;background:var(--backdrop-light);font-family:"Roboto Condensed",sans-serif}
  .backdrop{position:absolute;inset:0}

  .label{position:absolute;left:72px;top:439px;width:1062px;height:313px;background:var(--cream);
    box-shadow:-6px 6px 12px rgba(0,0,0,.45)}
  .gold-band{position:absolute;left:0;width:100%;height:7px;z-index:2;
    background:linear-gradient(90deg,var(--gold-dark),var(--gold-light) 20%,var(--gold-dark) 40%,var(--gold-light) 62%,var(--gold-dark) 80%,var(--gold-light))}
  .gold-band.top{top:0}
  .gold-band.bottom{bottom:0}

  .leaf-pattern{position:absolute;border-radius:50%;background:radial-gradient(ellipse at center,rgba(208,150,130,.18),rgba(208,150,130,0) 70%)}

  /* back panel */
  .nutrition{position:absolute;left:30px;top:21px;width:130px;height:272px;border:1px solid var(--ink);
    background:linear-gradient(135deg,#c98d8d,#f6dadd 45%,#e9b4b7 75%,#f8e1e3);
    font-family:"Arimo",sans-serif;color:var(--ink);padding:3px 4px}
  .nutrition h2{font-size:16.5px;font-weight:700;line-height:19px;letter-spacing:-.2px;white-space:nowrap}
  .nf-serving{font-size:6px;padding-left:1px}
  .nf-bar{height:5px;background:var(--ink);margin:2px 0}
  .nf-bar.thin{height:2px}
  .nf-amount{font-size:6.5px;font-weight:700;margin-top:5px}
  .nf-calories{display:flex;justify-content:space-between;font-size:14px;font-weight:700;line-height:16px}
  .nf-dv{font-size:5px;font-weight:700;text-align:right;border-bottom:1px solid #555;padding:2px 0}
  .nf-row{font-size:5.8px;line-height:10.2px;border-bottom:1px solid #555}
  .nf-row b{font-weight:700}
  .nf-row.indent{padding-left:8px}
  .nf-vitamins{font-size:5.4px;line-height:9px;border-bottom:1px solid #555;display:flex;justify-content:space-between}
  .nf-ingredients{font-size:6.3px;line-height:8.3px;margin-top:3px}

  .back-note{position:absolute;left:154px;width:220px;text-align:center;font-size:11.2px;color:var(--brown-text);line-height:15px;white-space:nowrap}
  .barcode-space{position:absolute;left:203px;top:253px;width:123px;height:30px;background:#fff}

  /* front panel */
  .front{position:absolute;left:371px;top:7px;width:389px;height:299px;background:var(--brown);overflow:hidden}
  .front .leaf-pattern{background:radial-gradient(ellipse at center,rgba(140,80,40,.35),rgba(140,80,40,0) 70%)}
  .brand-name{position:absolute;left:0;right:0;top:96px;text-align:center;color:var(--cream-ink);
    font-weight:400;text-transform:uppercase}
  .brand-line-main{display:block;font-size:40px;line-height:48px;letter-spacing:4px}
  .brand-line-sub{display:block;font-size:20px;line-height:24px;letter-spacing:4px;margin-top:6px}
  .brand-mark{display:inline-block;width:11px;height:11px;border-radius:50%;background:var(--cream-ink);margin-right:12px;vertical-align:8px}
  .est{position:absolute;left:0;right:0;top:183px;display:flex;justify-content:center;align-items:center;gap:8px;
    color:var(--cream-ink);font-size:10px;letter-spacing:1.2px;font-weight:400;line-height:14px}
  .est::before,.est::after{content:"";width:22px;height:1px;background:var(--cream-ink)}
  .product-name{position:absolute;left:0;right:0;top:202px;text-align:center;color:var(--pink);
    font-weight:300;font-size:48px;line-height:58px;letter-spacing:0;text-transform:uppercase;white-space:nowrap}
  .front-foot{position:absolute;bottom:4px;left:47px;right:52px;display:flex;justify-content:space-between;
    color:var(--cream-ink);font-size:10.5px;font-weight:300}

  /* side panel */
  .story{position:absolute;left:799px;top:42px;width:232px;font-size:11.3px;line-height:15.2px;color:var(--brown-text)}
  .qr-space{position:absolute;left:850px;top:145px;width:127px;height:127px;background:#fff;
    border:2px solid transparent;border-image:linear-gradient(135deg,var(--gold-dark),var(--gold-light),var(--gold-dark)) 1}
</style>
</head>
<body>
<svg class="backdrop" width="1200" height="1200" viewBox="0 0 1200 1200" aria-hidden="true">
  <polygon points="1200,18 1200,1200 18,1200" fill="var(--backdrop-dark)"/>
</svg>

<div class="label">
  <div class="gold-band top"></div>

  <div class="leaf-pattern" role="img" aria-label="Faint tropical leaf pattern" style="left:160px;top:40px;width:220px;height:240px"></div>
  <div class="leaf-pattern" role="img" aria-label="Faint tropical leaf pattern" style="left:300px;top:110px;width:140px;height:190px"></div>
  <div class="leaf-pattern" role="img" aria-label="Faint tropical leaf pattern" style="left:860px;top:60px;width:190px;height:200px"></div>

  <section class="back-panel">
    <div class="nutrition">
      <h2>Nutrition Facts</h2>
      <div class="nf-serving">Serving Size 1 serving</div>
      <div class="nf-bar"></div>
      <div class="nf-amount">Amount Per Serving</div>
      <div class="nf-calories"><span>Calories</span><span>150</span></div>
      <div class="nf-bar thin"></div>
      <div class="nf-dv">%Daily Value*</div>
      <div class="nf-row"><b>Total Fat</b> 13g</div>
      <div class="nf-row indent">Saturated Fat 8g</div>
      <div class="nf-row indent">Trans Fat 0g</div>
      <div class="nf-row"><b>Cholesterol</b> 55mg</div>
      <div class="nf-row"><b>Sodium</b> 5mg</div>
      <div class="nf-row"><b>Total Carbohydrate</b> 10g</div>
      <div class="nf-row indent">Dietary Fiber 0g</div>
      <div class="nf-row indent">Total Sugars 9g</div>
      <div class="nf-row indent">Includes Added Sugars 8g</div>
      <div class="nf-row"><b>Protein</b> 1g</div>
      <div class="nf-bar thin"></div>
      <div class="nf-vitamins"><span>• &nbsp; Vitamin D 10% DV</span><span>• &nbsp; Calcium 2% DV</span></div>
      <div class="nf-vitamins"><span>• &nbsp; Iron 0% DV •</span><span>Potassium 1% DV &nbsp;&nbsp;&nbsp;</span></div>
      <p class="nf-ingredients"><b>Ingredients</b>: Guava concentrate, Unsalted butter (cream, natural flavor), Cane sugar, Whole eggs, Egg yolks, Proprietary blend of natural flavors and spices.</p>
    </div>
    <p class="back-note" style="top:106px">Manufactured by<br>Lanakila Sweet Kitchen, Hawaiʻi.</p>
    <p class="back-note" style="top:168px">Keep Refrigerated.</p>
    <div class="barcode-space"></div>
  </section>

  <section class="front">
    <div class="leaf-pattern" role="img" aria-label="Faint tropical leaf pattern" style="left:-40px;top:100px;width:160px;height:200px"></div>
    <div class="leaf-pattern" role="img" aria-label="Faint tropical leaf pattern" style="left:260px;top:20px;width:180px;height:220px"></div>
    <div class="brand-name">
      <span class="brand-line-main"><span class="brand-mark"></span>Lanakila</span>
      <span class="brand-line-sub">Sweet Kitchen</span>
    </div>
    <div class="est">EST 1999</div>
    <h1 class="product-name">Mellow Spread</h1>
    <div class="front-foot"><span>Net Wt. 8 oz (227g)</span><span>Made in Hawaiʻi</span></div>
  </section>

  <section class="side-panel">
    <p class="story">Lanakila Sweet Kitchen brings authentic island flavors to every table. Our signature Mellow Spread blends tropical fruit and fresh cream for a taste of pure aloha.</p>
    <div class="qr-space"></div>
  </section>

  <div class="gold-band bottom"></div>
</div>
</body>
</html>
```